Family Owned Construction Company Needs Modern Business Cards

We need a new design for our business cards. We are a family owned construction company, Brantwell Construction, based in Mendon, Vermont and would like to add in our new logo and find a more modern look. We also want to use our old to make sure people know who we are. We do site development, highway, environmental, demolition, utility and aggregate.

Contact Information for Business Card

We want to have the office address, 418 Quarry Ridge Road, Larkfield Hollow 05788 and our phone (802) 555-0137 and fax (802) 555-0164 on there as well. Our website is www.brantwellinc.example. There should be a place for the person's name, title, cell number, and email address on the card. Words that we would like to be associated with our company are honesty, predictable, reliable, integrity, dedicated, built right quality, consistent, whatever it takes, and innovation. Safety is also very important to us.

Font styles to use
Serif
Sans Serif
Other font styles liked:
• Square 721 Extented

Colors
0255a3
ffffff

Requirements
Must have
• Office address, phone number and fax number. New logo with excavator
Nice to have
• That we do site development, highway, environmental, demolition, utility, and aggregate. Both logos

```html
<!DOCTYPE html>
<html lang="en">
<head>
<meta charset="utf-8">
<title>Brantwell Construction – Business Cards</title>
<link href="https://fonts.googleapis.com/css2?family=Michroma&family=Montserrat:wght@400;800&display=swap" rel="stylesheet">
<style>
  :root {
    --navy: #1e3566;
    --white: #ffffff;
    --page: #e9ebef;
    --card-shadow: rgba(20, 30, 55, 0.18);
  }
  html, body {
    margin: 0;
    padding: 0;
    width: 1200px;
    height: 880px;
    overflow: hidden;
    background: var(--page);
  }
  .canvas {
    position: relative;
    width: 1200px;
    height: 880px;
  }
  .card {
    position: absolute;
    left: 250px;
    width: 700px;
    height: 400px;
    background: var(--white);
    box-shadow: 0 6px 18px var(--card-shadow);
    overflow: hidden;
    color: var(--navy);
  }
  .card--front { top: 20px; }
  .card--back { top: 460px; }

  .brand {
    position: absolute;
    left: 0; right: 0;
    display: flex;
    align-items: center;
    justify-content: center;
    gap: 12px;
  }
  .brand-mark {
    flex: none;
    width: 20px;
    height: 20px;
    background: var(--navy);
  }
  .brand-name {
    font-family: "Michroma", sans-serif;
    font-size: 23px;
    letter-spacing: 0.5px;
    color: var(--navy);
    text-transform: uppercase;
    white-space: nowrap;
  }

  /* Front */
  .front-brand { top: 120px; }
  .services {
    position: absolute;
    left: 0; right: 0;
    top: 220px;
    text-align: center;
    font-family: "Michroma", sans-serif;
    font-size: 14px;
    line-height: 1.6;
  }
  .services__title {
    font-family: "Montserrat", sans-serif;
    font-weight: 800;
    font-size: 15px;
    letter-spacing: 1px;
    margin-bottom: 10px;
  }

  /* Back */
  .back-brand { top: 130px; }
  .back-brand .brand-name { font-size: 21px; }
  .info-band {
    position: absolute;
    left: 0; right: 0; bottom: 0;
    height: 96px;
    background: var(--navy);
    color: var(--white);
    display: flex;
    align-items: center;
    padding: 0 28px;
    box-sizing: border-box;
  }
  .person__name {
    font-family: "Montserrat", sans-serif;
    font-weight: 800;
    font-size: 21px;
    letter-spacing: 1px;
    text-transform: uppercase;
    white-space: nowrap;
  }
  .person__title {
    font-family: "Montserrat", sans-serif;
    font-size: 15px;
    white-space: nowrap;
  }
  .divider {
    flex: none;
    width: 1px;
    height: 44px;
    background: var(--white);
    margin: 0 20px;
  }
  .contact-list,
  .address {
    font-family: "Michroma", sans-serif;
    font-size: 12px;
    line-height: 1.8;
    white-space: nowrap;
  }
  .contact-list__row {
    display: flex;
    align-items: center;
    gap: 8px;
  }
  .contact-list__row svg { width: 13px; height: 13px; }
</style>
</head>
<body>
<main class="canvas">

  <section class="card card--front" aria-label="Business card front">
    <div class="brand front-brand">
      <span class="brand-mark"></span>
      <span class="brand-name">Brantwell Construction</span>
    </div>
    <div class="services">
      <div class="services__title">WE DO</div>
      <div>site development, highway, environmental, demolition</div>
      <div>utility and aggregate.</div>
    </div>
  </section>

  <section class="card card--back" aria-label="Business card back">
    <div class="brand back-brand">
      <span class="brand-mark"></span>
      <span class="brand-name">Brantwell Construction</span>
    </div>

    <div class="info-band">
      <div class="person">
        <div class="person__name">Jordan Hale</div>
        <div class="person__title">Managing Director</div>
      </div>
      <span class="divider"></span>
      <div class="contact-list">
        <div class="contact-list__row">
          <svg viewBox="0 0 24 24" aria-hidden="true"><path fill="#ffffff" d="M6.6 10.8a15 15 0 0 0 6.6 6.6l2.2-2.2a1 1 0 0 1 1-.25 11.4 11.4 0 0 0 3.6.57 1 1 0 0 1 1 1V20a1 1 0 0 1-1 1A17 17 0 0 1 3 4a1 1 0 0 1 1-1h3.5a1 1 0 0 1 1 1c0 1.25.2 2.45.57 3.57a1 1 0 0 1-.25 1z"/></svg>
          <span>(802) 555-0137</span>
        </div>
        <div class="contact-list__row">
          <svg viewBox="0 0 24 24" aria-hidden="true"><path fill="#ffffff" d="M6 3h9l3 3v4H6zM4 11h16a2 2 0 0 1 2 2v6H2v-6a2 2 0 0 1 2-2zm3 3v2h4v-2z"/></svg>
          <span>(802) 555-0164</span>
        </div>
      </div>
      <span class="divider"></span>
      <div class="address">
        <div>418 Quarry Ridge Road,</div>
        <div>Larkfield Hollow 05788</div>
      </div>
    </div>
  </section>

</main>
</body>
</html>
```